Regional Valuation Adjustments - displaying differences in US regions by equipment category

We need a short flyer that illustrates how our business divides the country into regions, and for each region, how it differs from average across key equipment categories. Fairly straightforward, doesn't require a lot of fluff.

Target Market(s)

Construction companies and equipment owners

Industry/Entity Type

Construction

Font styles to use
Serif

Colors

Designer to choose colors to be used in the design.

Requirements
Must have
• - Header saying Brindle Sales - Regional Valuation Adjustments
• - Nice looking map (maybe half page?) showing the USA, divided into different colored regions (per the ppt document). Region breakpoints should pop a bit, maybe with negative space between them
• - Section for each region: Midwest, Northeast, Northwest, Southeast, Southwest, West)
• - Each section should show the 25 adjustment factors, organized by Category Group.
• - Show the adjustment factors as (1 - factor), so 102% shows as +2%, and 98% shows as -2%, with + or - sign included.
• - Show the factors as something more than just a number -- maybe a bar chart (above or below the 0 line, if its positive or negative)
• - Display the Global factor as "All Other" (do not use word "global"), and display it last.
Nice to have
• - Attached a sample flyer we have used in the past, could be used to guide look and feel

```html
<!DOCTYPE html>
<html lang="en">
<head>
<meta charset="utf-8">
<title>Brindle Sales – Regional Valuation Adjustments</title>
<link rel="stylesheet" href="https://fonts.googleapis.com/css2?family=Open+Sans:ital,wght@0,600;0,700;0,800;1,700;1,800&display=swap">
<style>
  :root {
    --gold: #9b7a34;
    --ink: #2b2119;
    --paper: #ffffff;
    --midwest: #fefea8;
    --northeast: #a9f8a9;
    --northwest: #fdaafd;
    --southeast: #7efcfc;
    --southwest: #7fd6fe;
    --west: #ababf7;
  }
  * { margin: 0; padding: 0; box-sizing: border-box; }
  html, body { width: 924px; height: 1200px; overflow: hidden; background: var(--paper); }
  body { font-family: "Open Sans", Arial, sans-serif; color: var(--ink); }

  .flyer { position: relative; width: 924px; height: 1200px; }

  .brand {
    position: absolute; left: 48px; top: 30px;
    display: flex; align-items: center; gap: 12px;
    color: var(--ink);
  }
  .brand-mark { width: 22px; height: 22px; background: var(--gold); flex: none; }
  .brand-name {
    font-weight: 800; font-size: 38px; line-height: 40px; letter-spacing: 1px;
  }
  .brand-name span { display: block; }

  .title-band { position: absolute; left: 0; top: 0; width: 924px; height: 140px; }
  .title-text {
    position: absolute; left: 300px; top: 0; width: 624px; height: 140px;
    color: #fff; font-style: italic; text-transform: uppercase; line-height: 1;
  }
  .title-text .line-1 {
    position: absolute; right: 64px; top: 12px;
    font-size: 52px; font-weight: 800;
  }
  .title-text .line-2 {
    position: absolute; right: 56px; top: 72px;
    font-size: 35px; font-weight: 700;
  }

  .region-map {
    position: absolute; left: 40px; top: 156px; width: 848px; height: 508px;
    background: linear-gradient(120deg, var(--northwest) 0%, var(--west) 25%, var(--southwest) 45%, var(--midwest) 60%, var(--southeast) 80%, var(--northeast) 100%);
    opacity: .55; border-radius: 6px;
  }

  .adjustments {
    position: absolute; left: 14px; top: 686px; width: 896px;
    border-collapse: collapse; table-layout: fixed;
    border: 2px solid var(--ink);
  }
  .adjustments th {
    background: var(--gold); color: #fff; font-weight: 700; font-size: 16px;
    height: 32px; border: 1.5px solid var(--ink); border-bottom-width: 5px;
    text-align: center;
  }
  .adjustments td {
    height: 18.4px; font-size: 13.5px; font-weight: 600; line-height: 1;
    border-left: 1.5px solid var(--ink); border-bottom: 1px solid var(--ink);
    text-align: right; padding-right: 40px;
  }
  .adjustments td.category {
    text-align: left; padding: 0 0 0 12px; font-weight: 700; font-size: 14px;
    background: var(--paper);
  }
  .adjustments td:nth-child(2) { background: var(--midwest); }
  .adjustments td:nth-child(3) { background: var(--northeast); }
  .adjustments td:nth-child(4) { background: var(--northwest); }
  .adjustments td:nth-child(5) { background: var(--southeast); }
  .adjustments td:nth-child(6) { background: var(--southwest); }
  .adjustments td:nth-child(7) { background: var(--west); padding-right: 30px; }
  .adjustments tbody tr:first-child td { padding-top: 4px; }
</style>
</head>
<body>
<main class="flyer">
  <div class="brand">
    <span class="brand-mark"></span>
    <div class="brand-name"><span>BRINDLE</span><span>SALES</span></div>
  </div>

  <svg class="title-band" viewBox="0 0 924 140" aria-hidden="true">
    <polygon points="340,0 924,0 924,140 300,140" fill="var(--gold)"/>
  </svg>
  <h1 class="title-text">
    <span class="line-1">Regional</span>
    <span class="line-2">Valuation Adjustments</span>
  </h1>

  <div class="region-map" role="img" aria-label="Map of the contiguous United States divided into six coloured regions: Northwest, West, Southwest, Midwest, Southeast and Northeast"></div>

  <table class="adjustments">
    <colgroup>
      <col style="width:240px"><col style="width:110px"><col style="width:110px"><col style="width:108px"><col style="width:111px"><col style="width:111px"><col style="width:106px">
    </colgroup>
    <thead>
      <tr><th>CATEGORY</th><th>Midwest</th><th>Northeast</th><th>Northwest</th><th>Southeast</th><th>Southwest</th><th>West</th></tr>
    </thead>
    <tbody>
      <tr><td class="category">ARTICULATING BOOMS</td><td>+1.9%</td><td>-.2%</td><td>+4%</td><td>+2.7%</td><td>-6%</td><td>+2.3%</td></tr>
      <tr><td class="category">SCISSOR LIFTS</td><td>-.4%</td><td>-5.4%</td><td>+3.1%</td><td>-2.4%</td><td>+.6%</td><td>+3.7%</td></tr>
      <tr><td class="category">TELESCOPIC BOOMS</td><td>-3.3%</td><td>-.3%</td><td>+1.6%</td><td>-.6%</td><td>+.4%</td><td>+2.7%</td></tr>
      <tr><td class="category">TOWABLE BOOMS</td><td>-3.3%</td><td>-.3%</td><td>+1.6%</td><td>-.6%</td><td>+.4%</td><td>+2.7%</td></tr>
      <tr><td class="category">ARTICULATED TRUCKS</td><td>+2%</td><td>+.6%</td><td>+7.2%</td><td>-1.8%</td><td>-3%</td><td>+4.1%</td></tr>
      <tr><td class="category">BACKHOE LOADERS</td><td>-.7%</td><td>-1.5%</td><td>+5.7%</td><td>-1.7%</td><td>-.5%</td><td>+2.4%</td></tr>
      <tr><td class="category">CRAWLER LOADERS</td><td>+4.5%</td><td>+3.7%</td><td>+3.3%</td><td>-1.3%</td><td>-2.5%</td><td>+7.5%</td></tr>
      <tr><td class="category">DOZERS</td><td>+4.5%</td><td>+3.7%</td><td>+3.3%</td><td>-1.3%</td><td>-2.5%</td><td>+7.5%</td></tr>
      <tr><td class="category">EXCAVATORS</td><td>+2%</td><td>+.6%</td><td>+7.2%</td><td>-1.8%</td><td>-3%</td><td>+4.1%</td></tr>
      <tr><td class="category">MOTOR GRADERS</td><td>+2%</td><td>+.6%</td><td>+7.2%</td><td>-1.8%</td><td>-3%</td><td>+4.1%</td></tr>
      <tr><td class="category">RIGID TRUCKS</td><td>+2%</td><td>+.6%</td><td>+7.2%</td><td>-1.8%</td><td>-3%</td><td>+4.1%</td></tr>
      <tr><td class="category">SCRAPERS</td><td>+2%</td><td>+.6%</td><td>+7.2%</td><td>-1.8%</td><td>-3%</td><td>+4.1%</td></tr>
      <tr><td class="category">SKID STEER LOADERS</td><td>+.4%</td><td>+1.3%</td><td>+7.5%</td><td>-3.3%</td><td>-3%</td><td>+2%</td></tr>
      <tr><td class="category">TRACK LOADER</td><td>+1.9%</td><td>-.6%</td><td>+5.6%</td><td>-1.3%</td><td>-3%</td><td>+5.2%</td></tr>
      <tr><td class="category">WHEEL DOZERS</td><td>+.1%</td><td>+2.6%</td><td>+7.5%</td><td>-4.2%</td><td>-2.5%</td><td>+4.6%</td></tr>
      <tr><td class="category">WHEEL EXCAVATORS</td><td>+2%</td><td>+.6%</td><td>+7.2%</td><td>-1.8%</td><td>-3%</td><td>+4.1%</td></tr>
      <tr><td class="category">WHEEL LOADERS</td><td>+.1%</td><td>+2.6%</td><td>+7.5%</td><td>-4.2%</td><td>-2.5%</td><td>+4.6%</td></tr>
      <tr><td class="category">FORKLIFT TRUCKS</td><td>-2.4%</td><td>-1%</td><td>+.9%</td><td>-.6%</td><td>+3.2%</td><td>-1.1%</td></tr>
      <tr><td class="category">MAST LIFTS</td><td>-.4%</td><td>-5.4%</td><td>+3.1%</td><td>-2.4%</td><td>+.6%</td><td>+3.7%</td></tr>
      <tr><td class="category">ROUGH-TERRAIN FORKLIFTS</td><td>-2.5%</td><td>-.8%</td><td>+3.7%</td><td>-1.2%</td><td>-3.2%</td><td>+7.5%</td></tr>
      <tr><td class="category">TELEHANDLERS</td><td>-2.5%</td><td>-.8%</td><td>+3.7%</td><td>-1.2%</td><td>-3.2%</td><td>+7.5%</td></tr>
      <tr><td class="category">ALL OTHER</td><td>-1.3%</td><td>-1.6%</td><td>+2.8%</td><td>-.3%</td><td>-1.2%</td><td>+2.8%</td></tr>
      <tr><td class="category">LIGHTING EQUIPMENT</td><td>-3.9%</td><td>-.7%</td><td>-4.4%</td><td>+2.6%</td><td>-1.8%</td><td>+7.5%</td></tr>
      <tr><td class="category">PICKUP TRUCKS</td><td>-5%</td><td>-7.5%</td><td>+5.2%</td><td>+3.8%</td><td>-4.2%</td><td>+4.9%</td></tr>
      <tr><td class="category">TRUCK TRACTORS</td><td>-3.1%</td><td>-5.3%</td><td>+5.2%</td><td>-1.5%</td><td>+2.3%</td><td>-.2%</td></tr>
    </tbody>
  </table>
</main>
</body>
</html>
```